Tri-fold Brochure for Law Firm

Double-sided brochure to be folded into 6 sides tri-fold brochure for an estate planning special for new parents or parents-to-be. Brochure will be placed in classes for new parents/young parents.

Target Market(s)

New Parents Aged 24-34

Industry/Entity Type

Law Firm

Font styles to use
Serif

Requirements
Must have
• The information provided in the word document.
Nice to have
• Highlight the phrase "for New Parents."
• You may use the color scheme from our website:
• http://k27.9qd.sitehostbox.net/

```html
<!DOCTYPE html>
<html lang="en">
<head>
<meta charset="utf-8">
<title>Penning Legal – Estate Planning for New Parents</title>
<link rel="stylesheet" href="https://fonts.googleapis.com/css2?family=Bodoni+Moda:wght@400;600;700&family=Open+Sans:wght@400&family=Kalam:wght@400&display=swap">
<style>
  :root {
    --gold: #efbb3c;
    --gold-deep: #e3aa2a;
    --espresso: #2e2520;
    --ink: #2b2b2b;
    --paper: #ffffff;
    --room-light: #f4f2ef;
    --room-mid: #e6e1da;
    --portrait: #4a4540;
  }
  html, body { margin: 0; padding: 0; overflow: hidden; }
  body { width: 1200px; height: 870px; background: var(--paper); }
  .brochure { position: relative; width: 1200px; height: 870px; overflow: hidden; font-family: "Open Sans", Arial, sans-serif; color: var(--ink); }
  .brochure__art { position: absolute; inset: 0; }
  .fold { position: absolute; top: 0; bottom: 0; width: 14px; background: linear-gradient(to right, rgba(0,0,0,0.07), rgba(0,0,0,0)); }
  .fold--one { left: 400px; }
  .fold--two { left: 800px; }

  .attorney-name { position: absolute; left: 258px; top: 255px; font-family: "Kalam", cursive; font-size: 18px; line-height: 24px; color: #fff; text-align: right; width: 104px; }

  .label-bar { position: absolute; left: 18px; top: 484px; width: 366px; height: 45px; background: var(--espresso); border-radius: 6px; box-shadow: 0 4px 6px rgba(0,0,0,0.25); }
  .label-bar__inner { position: absolute; inset: 5px 7px; border: 1px solid var(--gold); border-radius: 3px; display: flex; align-items: center; justify-content: center; font-family: "Bodoni Moda", serif; font-size: 17px; color: #f5efe4; letter-spacing: 0.5px; }

  .why-copy { position: absolute; left: 37px; top: 562px; width: 324px; font-size: 14.5px; line-height: 21px; text-align: justify; }
  .why-copy p { margin: 0 0 12px; }
  .why-copy p:first-child { text-align: left; }

  .firm-name { font-family: "Bodoni Moda", serif; font-weight: 700; color: var(--ink); }
  .firm-name--contact { position: absolute; left: 416px; top: 636px; font-size: 16px; }

  .contact-list { position: absolute; left: 420px; top: 680px; margin: 0; padding: 0; list-style: none; font-size: 13.5px; line-height: 19px; }
  .contact-list li { display: flex; align-items: flex-start; gap: 6px; margin-bottom: 4px; }
  .contact-list svg { flex: none; margin-top: 3px; }

  .web-pill { position: absolute; left: 424px; top: 812px; width: 273px; height: 33px; background: var(--espresso); border-radius: 5px; box-shadow: 0 4px 6px rgba(0,0,0,0.25); }
  .web-pill__inner { position: absolute; inset: 4px 6px; border: 1px solid var(--gold); border-radius: 3px; display: flex; align-items: center; justify-content: center; color: #fff; font-size: 14px; letter-spacing: 2.5px; }

  .seal-name { position: absolute; left: 861px; top: 604px; width: 230px; text-align: center; font-size: 20px; }

  .offer { position: absolute; left: 808px; top: 706px; width: 384px; text-align: center; font-family: "Bodoni Moda", serif; color: var(--ink); }
  .offer__title { margin: 0; font-size: 17px; font-weight: 400; }
  .offer__highlight { font-size: 22px; font-weight: 700; }
  .offer__price { margin: 8px 0 4px; font-size: 30px; font-weight: 700; }
  .offer__note { margin: 0; font-size: 16.5px; line-height: 24px; }
</style>
</head>
<body>
<main class="brochure">
  <svg class="brochure__art" width="1200" height="870" viewBox="0 0 1200 870">
    <defs>
      <linearGradient id="room" x1="0" y1="0" x2="1" y2="1">
        <stop offset="0" stop-color="var(--room-light)"/>
        <stop offset="0.6" stop-color="#efe9e3"/>
        <stop offset="1" stop-color="var(--room-mid)"/>
      </linearGradient>
      <radialGradient id="portraitTone" cx="0.45" cy="0.5" r="0.6">
        <stop offset="0" stop-color="#6b5148"/>
        <stop offset="1" stop-color="var(--portrait)"/>
      </radialGradient>
    </defs>
    <rect width="1200" height="870" fill="url(#room)" role="img" aria-label="Photo of a smiling young family with two children and a baby on a white sofa in a bright living room"/>
    <path class="page-white" fill="var(--paper)" d="M0,290 C60,220 170,160 300,180 C400,200 480,280 560,420 C640,560 700,720 800,870 L0,870 Z"/>
    <path class="swoosh" fill="var(--gold)" d="M0,200 C80,110 260,60 420,125 C520,170 565,300 640,420 C720,540 780,565 880,585 C960,600 1080,560 1200,480 L1200,870 L800,870 C700,720 640,560 560,420 C480,280 400,200 300,180 C170,160 60,220 0,290 Z"/>
    <path fill="none" stroke="#d9a42c" stroke-width="1" d="M560,430 C640,570 700,720 790,870"/>
    <path fill="none" stroke="#d9a42c" stroke-width="1" d="M620,470 C700,600 760,600 880,620 C980,630 1090,590 1200,520"/>
    <ellipse cx="212" cy="300" rx="200" ry="188" fill="none" stroke="var(--espresso)" stroke-width="1.4"/>
    <circle cx="200" cy="290" r="172" fill="var(--gold)"/>
    <circle cx="200" cy="290" r="165" fill="url(#portraitTone)" role="img" aria-label="Portrait photo of attorney Laura J. Penning"/>
    <circle cx="976" cy="559" r="130" fill="none" stroke="#fff" stroke-width="1.2"/>
    <circle cx="976" cy="559" r="117" fill="var(--paper)" stroke="var(--gold-deep)" stroke-width="4"/>
  </svg>
  <div class="fold fold--one"></div>
  <div class="fold fold--two"></div>

  <div class="attorney-name">Laura J.<br>Penning</div>

  <div class="label-bar"><div class="label-bar__inner">Why should every parent have a will?</div></div>
  <div class="why-copy">
    <p>Imagine how many people love your children.</p>
    <p>Would there be a fight over who would care for your children if you passed away without leaving instructions?</p>
    <p>Naming a guardian in your will helps avoid litigation that would cause additional stress to your children and loved ones. You can also name a back-up in the event that your first choice is unable or unwilling to serve as guardian.</p>
  </div>

  <div class="firm-name firm-name--contact">Penning Legal, llc</div>
  <ul class="contact-list">
    <li><svg width="14" height="16" viewBox="0 0 14 16"><path d="M7 1a5 5 0 0 0-5 5c0 4 5 9 5 9s5-5 5-9a5 5 0 0 0-5-5z" fill="none" stroke="var(--gold-deep)" stroke-width="2"/></svg><span>48 E. Chesterfield Road,<br>Suite 310, Easton, MD 21601</span></li>
    <li><svg width="14" height="16" viewBox="0 0 14 16"><rect x="3" y="1" width="8" height="14" rx="2" fill="none" stroke="var(--gold-deep)" stroke-width="2"/></svg><span>(410)-555-0143</span></li>
    <li><svg width="14" height="16" viewBox="0 0 14 16"><path d="M4 1c5 1 6 12 0 14" fill="none" stroke="var(--gold-deep)" stroke-width="2.4" stroke-linecap="round"/></svg><span>(410)-555-0187</span></li>
    <li><svg width="14" height="16" viewBox="0 0 14 16"><rect x="1" y="4" width="12" height="9" fill="none" stroke="var(--gold-deep)" stroke-width="1.6"/><path d="M1 4l6 5 6-5" fill="none" stroke="var(--gold-deep)" stroke-width="1.6"/></svg><span>laura@penning-legal.com</span></li>
  </ul>
  <div class="web-pill"><div class="web-pill__inner">www.penning-legal.com</div></div>

  <div class="firm-name seal-name">Penning Legal, llc</div>

  <section class="offer">
    <h1 class="offer__title">Estate Planning Special for <span class="offer__highlight">New Parents</span></h1>
    <p class="offer__price">$750 per couple</p>
    <p class="offer__note">For parents-to-be and parents of children<br>under 5 years old.</p>
  </section>
</main>
</body>
</html>
```